Re-Design Business Card and Logo for Plastic Printing

Business is a small financial planning (investments, insurance, retirement, etc.) firm. The majority of our clients are 55+ years old, professional occupations (pilots, doctors, bankers, etc.) but not necessarily "high net worth."
I would like to have a design that would be used on clear plastic business cards. I have found a vendor that makes these but I do not have the ability to design these like I want.
I do have one proof but I just don't feel like it's the right one for me. Also, I feel that I need some help with a logo redesign so maybe someone could handle that for me as well.
I want the final design to "eye catching" but still be tasteful. I am open to suggestion regarding colors and such.
I will include the old design as well as the new proof I have to give you an idea of what I current have. Keep in mind, I have no allegiance to the attached designs.
For the second file (Business Card New Proof), the white space shown will be transparent when printed on plastic card.
Target Market(s)
Mostly people age 55+ in professional occupations.
Industry/Entity Type
Financial Service
Contact Information for Business Card
Looking for design that can be printed on clear plastic cards (if possible).
Logo Text
KLT - Kestrel Lakeview Trust
Requirements
Must have
- Must be double sided because disclosure is required for compliance reasons.
Designations (must include the Registered trademark symbol as follows)...
MBA, ChFC®, CLU®, CRPS®
Nice to have
- The little icons next to email, phone and fax are nice.
Should not have
- I think I would like to eliminate the Owner and Co-Founder line that you see on the attachments.

```html
<!DOCTYPE html>
<html lang="en">
<head>
<meta charset="utf-8">
<title>Kestrel Lakeview Trust – Business Card</title>
<link href="https://fonts.googleapis.com/css2?family=Montserrat:wght@500;700;800&family=Open+Sans:wght@400&display=swap" rel="stylesheet">
<style>
  :root {
    --brand-navy: #163d70;
    --brand-blue: #1f5c9c;
    --brand-ink: #1b2230;
    --card-white: #ffffff;
    --stage: #d9dbde;
    --rule: #2a2f38;
  }
  * { box-sizing: border-box; margin: 0; padding: 0; }
  html, body { width: 1200px; height: 965px; overflow: hidden; }
  body {
    background: var(--stage);
    display: flex;
    align-items: center;
    justify-content: center;
    gap: 30px;
    font-family: "Open Sans", sans-serif;
  }
  .card {
    width: 560px;
    height: 320px;
    position: relative;
    box-shadow: 0 6px 18px rgba(0,0,0,0.18);
    overflow: hidden;
  }

  /* Back side */
  .card-back { background: var(--brand-navy); }
  .back-brand {
    position: absolute;
    top: 112px;
    left: 0; right: 0;
    display: flex;
    align-items: center;
    justify-content: center;
    gap: 16px;
  }
  .back-dot {
    width: 64px; height: 64px;
    border: 4px solid var(--brand-blue);
    border-radius: 50%;
  }
  .back-name {
    font-family: "Montserrat", sans-serif;
    font-weight: 700;
    font-size: 40px;
    letter-spacing: 2px;
    color: var(--brand-blue);
  }
  .tagline {
    position: absolute;
    bottom: 44px;
    left: 0; right: 0;
    text-align: center;
    font-family: "Montserrat", sans-serif;
    font-weight: 500;
    font-size: 13px;
    letter-spacing: 0.6px;
    color: var(--card-white);
    text-transform: uppercase;
  }

  /* Front side */
  .card-front { background: var(--card-white); color: var(--brand-ink); }
  .brand {
    position: absolute;
    top: 30px;
    right: 32px;
    display: flex;
    align-items: center;
    gap: 12px;
  }
  .brand-dot {
    width: 44px; height: 44px;
    border: 4px solid var(--brand-navy);
    border-radius: 50%;
    flex: none;
  }
  .brand-name {
    font-family: "Montserrat", sans-serif;
    font-weight: 800;
    font-size: 20px;
    line-height: 1.1;
    color: var(--brand-navy);
    text-transform: uppercase;
    letter-spacing: 0.5px;
  }
  .divider {
    position: absolute;
    top: 172px;
    left: 290px;
    right: 32px;
    height: 1.5px;
    background: var(--rule);
  }
  .address {
    position: absolute;
    top: 188px;
    right: 32px;
    text-align: right;
    font-style: normal;
    font-size: 13px;
    line-height: 1.45;
  }
  .person {
    position: absolute;
    left: 30px;
    top: 150px;
  }
  .person-name {
    font-family: "Montserrat", sans-serif;
    font-weight: 700;
    font-size: 27px;
    color: var(--brand-navy);
    text-transform: uppercase;
    line-height: 1;
    white-space: nowrap;
  }
  .designations { font-size: 13px; margin-top: 5px; }
  .designations sup { font-size: 8px; }
  .contacts {
    position: absolute;
    left: 30px;
    bottom: 26px;
    list-style: none;
    font-size: 13.5px;
    line-height: 1.6;
  }
  .contacts li { display: flex; align-items: center; gap: 8px; }
  .contacts svg { width: 14px; height: 14px; flex: none; }
</style>
</head>
<body>
  <section class="card card-back" aria-label="Card back">
    <div class="back-brand">
      <span class="back-dot"></span>
      <span class="back-name">KLT</span>
    </div>
    <p class="tagline">Steady plans for every season ahead</p>
  </section>

  <section class="card card-front" aria-label="Card front">
    <div class="brand">
      <span class="brand-dot"></span>
      <span class="brand-name">Kestrel Lakeview<br>Trust</span>
    </div>
    <div class="person">
      <h1 class="person-name">Sam Holloway</h1>
      <p class="designations">MBA, ChFC<sup>®</sup>, CLU<sup>®</sup>, CRPS<sup>®</sup></p>
    </div>
    <div class="divider"></div>
    <address class="address">
      2180 Harbor Ridge Rd, Suite 310<br>Norfield, VA 23400
    </address>
    <ul class="contacts">
      <li>
        <svg viewBox="0 0 16 16" fill="none" stroke="#1f5c9c" stroke-width="1.4"><path d="M4 2l2 3-1.5 1.5a8 8 0 0 0 5 5L11 10l3 2-1.5 2.5C7 14 2 9 1.5 3.5z"/></svg>
        (555) 013-4821
      </li>
      <li>
        <svg viewBox="0 0 16 16" fill="#163d70"><rect x="4" y="1" width="8" height="5"/><rect x="1" y="7" width="14" height="8" rx="1"/></svg>
        (800) 555-0147 (Toll Free)
      </li>
      <li>
        <svg viewBox="0 0 16 16" fill="none" stroke="#1f5c9c" stroke-width="1.4"><rect x="1" y="3" width="14" height="10"/><path d="M1 3l7 6 7-6"/></svg>
        sholloway@kestrellakeview.com
      </li>
    </ul>
  </section>
</body>
</html>
```